Poster for homelessness project (2 day deadline)

Amber Lantern Scheme is an initiative in the UK which aims to ensure that people who are new to sleeping on the street are quickly given assistance to take them out of situation they find themselves in.

It began as a London-based project but is now being rolled out nationwide. I am working for a project based in the north of England.

We need some posters which show an image of a place where a rough sleeper may spend the night with some supporting graphic design.

I have three initial images, but I need to be able to easily swap out the images for others. I would appreciate if you could produce three posters for me, each with a different image.

-
Please note:
My client is quite vague about what they want at the moment and the above words may change. I need the selected product to be a layered raw file that I can amend myself with any Adobe CS5.5 (or below) application.

Any typefaces that you choose need to be easily purchasable online.

Please view formatinfo.pdf for formatting guidelines.

Target Market(s)

The general public. It will be placed in public places.

Industry/Entity Type

Graphic Design

Requirements
Must have
• Must contain the words:

"Tonight someone will sleep rough for the first time. Help us make sure they find the Amber Lantern."

"Would you sleep here? Sleeping rough is dangerous. Make sure everyone finds the Amber Lantern."

-
Nice to have
• I'd like this to be quite bleak, grimy and "urban" in feel.

You may recolour/tint the images in any way to enhance this feeling.

```html
<!DOCTYPE html>
<html lang="en">
<head>
<meta charset="utf-8">
<title>Would You Sleep Here? — Amber Lantern Scheme Poster</title>
<link href="https://fonts.googleapis.com/css2?family=Anton&family=Noto+Serif+Display:wdth,wght@62.5,500&display=swap" rel="stylesheet">
<style>
  :root {
    --paper: #ffffff;
    --ink: #141414;
    --band-grey: #808080;
    --panel-veil: rgba(255, 255, 255, 0.56);
    --brick-dark: #5a4d45;
    --brick-mid: #857a72;
    --brick-light: #a9a6a2;
    --bin-dark: #2b2e2d;
    --bin-mid: #4a4f4c;
    --bin-green: #5b7a5d;
    --ground: #3a3938;
  }
  html, body {
    margin: 0;
    padding: 0;
    overflow: hidden;
    background: var(--paper);
  }
  .poster {
    position: relative;
    width: 848px;
    height: 1200px;
    background: var(--paper);
    overflow: hidden;
  }
  .scene-photo {
    position: absolute;
    left: 12px;
    top: 17px;
    width: 824px;
    height: 956px;
    background:
      radial-gradient(ellipse 26% 18% at 12% 30%, rgba(225, 225, 222, 0.55), rgba(225, 225, 222, 0) 100%),
      radial-gradient(ellipse 22% 30% at 56% 62%, rgba(91, 122, 93, 0.55), rgba(91, 122, 93, 0) 100%),
      linear-gradient(180deg,
        rgba(0, 0, 0, 0) 0%,
        rgba(0, 0, 0, 0) 34%,
        rgba(43, 46, 45, 0.85) 42%,
        rgba(74, 79, 76, 0.9) 62%,
        rgba(43, 46, 45, 0.95) 82%,
        var(--ground) 100%),
      linear-gradient(90deg,
        var(--brick-dark) 0%,
        var(--brick-mid) 20%,
        var(--brick-light) 45%,
        var(--brick-mid) 66%,
        var(--brick-dark) 82%,
        var(--bin-dark) 100%);
  }
  .footer-band {
    position: absolute;
    left: 12px;
    top: 972px;
    width: 824px;
    height: 212px;
    background: var(--band-grey);
  }
  .message-panel {
    position: absolute;
    left: 218px;
    top: 17px;
    width: 412px;
    height: 955px;
    background: var(--panel-veil);
    text-align: center;
    color: var(--ink);
  }
  .headline {
    margin: 20px 0 0;
    font-family: "Anton", "Impact", sans-serif;
    font-weight: 400;
    font-size: 124px;
    line-height: 107px;
    letter-spacing: 1px;
    text-transform: uppercase;
  }
  .headline span {
    display: block;
    transform: scaleX(1.12);
  }
  .supporting-line {
    position: absolute;
    left: 0;
    right: 0;
    top: 694px;
    margin: 0;
    font-family: "Noto Serif Display", "Times New Roman", serif;
    font-stretch: 62.5%;
    font-variation-settings: "wdth" 62.5;
    font-weight: 500;
    font-size: 35px;
    line-height: 50px;
    text-transform: uppercase;
  }
  .supporting-line span { display: block; }
</style>
</head>
<body>
  <main class="poster">
    <div class="scene-photo" role="img" aria-label="Photograph of overflowing wheelie bins and rubbish bags against a grimy brick wall in a back alley"></div>
    <div class="footer-band"></div>
    <section class="message-panel">
      <h1 class="headline">
        <span>Would</span>
        <span>You</span>
        <span>Sleep</span>
        <span>Here?</span>
      </h1>
      <p class="supporting-line">
        <span>Sleeping rough</span>
        <span>is dangerous.</span>
        <span>Make sure everyone finds</span>
        <span>the Amber Lantern.</span>
      </p>
    </section>
  </main>
</body>
</html>
```